Customer Journey Graphic

I want to graphic to describe a marketing framework I am teaching a course on

It a framework for growing a business
The idea is we
get customers to "take a Journey" through 7 steps
to deliver value to them

There are 4 major concepts that impact this journey - Game Plan, Business Model, "Inside out thinking' and Unique Competitive advantage
These concepts can make the journey faster, get more people to take it or make it more valuable

The stages are

- Target
- attract
- nurture
- convert
- maximise
- loyalty
- reactivation

I want to uses this framework as an overall;; 'explainer' fro my idea ,so it must looks very professional, and work well in presentations

I have included a rought 'sketch; of my thinking as an attachment

Business Owners

Business

Serif

• clear, get acroess the idea of a Journye over times, teh idea you can improve your results throught applying concpets of ' business model', "inside out thinking: , unique competitive advantage and game plane

```html
<!DOCTYPE html>
<html lang="en">
<head>
<meta charset="utf-8">
<title>Growth Framework Cycle</title>
<link href="https://fonts.googleapis.com/css2?family=Russo+One&display=swap" rel="stylesheet">
<style>
  :root {
    --bg: #ffffff;
    --icon-tile: #56403d;
    --icon-mark: #ffffff;
    --label: #ffffff;
    --shadow: rgba(0, 0, 0, 0.22);
    --orange-deep: #e0561c;
    --orange-light: #f9a469;
    --blue-deep: #3a94d5;
    --blue-light: #6fc6fb;
    --red-deep: #e63d3f;
    --red-light: #fb7676;
    --green-light: #a9d046;
    --green-deep: #4c8d2f;
  }
  html, body {
    margin: 0;
    padding: 0;
    width: 1200px;
    height: 1200px;
    overflow: hidden;
    background: var(--bg);
  }
  .framework-cycle {
    display: block;
    width: 1200px;
    height: 1200px;
  }
  .concept-label {
    font-family: "Russo One", "Arial Black", sans-serif;
    font-size: 60px;
    fill: var(--label);
    text-anchor: middle;
  }
  .icon-tile { fill: var(--icon-tile); }
  .icon-line {
    fill: none;
    stroke: var(--icon-mark);
    stroke-width: 9;
    stroke-linecap: round;
    stroke-linejoin: round;
  }
  .icon-fill { fill: var(--icon-mark); }
</style>
</head>
<body>
<svg class="framework-cycle" viewBox="0 0 1300 1300" role="img" aria-label="Growth framework cycle: Inside Out Thinking, Unique Advantage, Business Model and Gameplan">
  <defs>
    <linearGradient id="grad-orange" x1="0" y1="1" x2="1" y2="0">
      <stop offset="0" stop-color="var(--orange-deep)"/>
      <stop offset="1" stop-color="var(--orange-light)"/>
    </linearGradient>
    <linearGradient id="grad-blue" x1="0" y1="0" x2="0" y2="1">
      <stop offset="0" stop-color="var(--blue-deep)"/>
      <stop offset="1" stop-color="var(--blue-light)"/>
    </linearGradient>
    <linearGradient id="grad-red" x1="0" y1="0" x2="0" y2="1">
      <stop offset="0" stop-color="var(--red-deep)"/>
      <stop offset="1" stop-color="var(--red-light)"/>
    </linearGradient>
    <linearGradient id="grad-green" x1="0" y1="0" x2="0" y2="1">
      <stop offset="0.1" stop-color="var(--green-light)"/>
      <stop offset="0.75" stop-color="var(--green-deep)"/>
    </linearGradient>
    <filter id="soft-shadow" x="-20%" y="-20%" width="140%" height="140%">
      <feDropShadow dx="6" dy="6" stdDeviation="7" flood-color="var(--shadow)"/>
    </filter>
  </defs>

  <!-- Concept segments -->
  <g class="segment segment-inside-out" filter="url(#soft-shadow)">
    <path fill="url(#grad-orange)" d="M190 507 A417 417 0 0 1 607 90 L607 188 L712 298 L607 410 L607 507 Z"/>
    <text class="concept-label" x="463" y="298">Inside Out</text>
    <text class="concept-label" x="467" y="362">Thinking</text>
  </g>

  <g class="segment segment-advantage" filter="url(#soft-shadow)">
    <path fill="url(#grad-blue)" d="M793 190 A417 417 0 0 1 1210 607 L1110 607 L1000 712 L890 607 L793 607 Z"/>
    <text class="concept-label" x="992" y="474">Unique</text>
    <text class="concept-label" x="992" y="538">Advantage</text>
  </g>

  <g class="segment segment-business-model" filter="url(#soft-shadow)">
    <path fill="url(#grad-red)" d="M1110 793 A417 417 0 0 1 692 1210 L692 1110 L588 1000 L692 895 L692 793 Z"/>
    <text class="concept-label" x="870" y="998">Business</text>
    <text class="concept-label" x="870" y="1062">Model</text>
  </g>

  <g class="segment segment-gameplan" filter="url(#soft-shadow)">
    <path fill="url(#grad-green)" d="M507 1108 A417 417 0 0 1 90 692 L188 692 L298 588 L410 692 L507 692 Z"/>
    <text class="concept-label" x="315" y="880">Gameplan</text>
  </g>

  <!-- Journey stage icons -->
  <g class="stage-icon icon-target" transform="translate(125 531)">
    <rect class="icon-tile" width="130" height="130"/>
    <circle class="icon-line" cx="65" cy="65" r="48"/>
    <circle class="icon-line" cx="65" cy="65" r="28"/>
    <circle class="icon-fill" cx="65" cy="65" r="10"/>
  </g>

  <g class="stage-icon icon-attract" transform="translate(367 531)">
    <rect class="icon-tile" width="130" height="130"/>
    <path class="icon-line" d="M35 45 L35 78 A30 30 0 0 0 95 78 L95 45" stroke-width="18" stroke-linecap="butt"/>
    <rect class="icon-fill" x="26" y="26" width="18" height="10"/>
    <rect class="icon-fill" x="86" y="26" width="18" height="10"/>
    <path class="icon-fill" d="M70 12 L56 50 L66 50 L60 72 L76 40 L66 40 L74 12 Z"/>
  </g>

  <g class="stage-icon icon-nurture" transform="translate(569 585)">
    <rect class="icon-tile" width="130" height="130"/>
    <path class="icon-fill" d="M4 48 L22 38 L36 72 L18 82 Z"/>
    <path class="icon-fill" d="M126 48 L108 38 L94 72 L112 82 Z"/>
    <path class="icon-line" d="M30 50 L52 44 L72 50 L94 46 M52 44 L46 58 Q54 64 64 56 L76 60 L96 74 M36 72 L50 84 M44 78 L58 92 M54 86 L66 98 M66 96 L74 100 M96 74 Q100 82 92 84 L80 78" stroke-width="6"/>
  </g>

  <g class="stage-icon icon-convert" transform="translate(751 645)">
    <rect class="icon-tile" width="130" height="130"/>
    <path class="icon-line" d="M65 78 L65 40" stroke-width="7"/>
    <path class="icon-fill" d="M65 58 Q40 52 42 24 Q66 30 65 58 Z"/>
    <path class="icon-fill" d="M66 52 Q70 22 92 16 Q96 46 66 52 Z"/>
    <path class="icon-line" d="M18 96 L40 88 L60 88 Q70 90 62 98 L48 98 M40 108 L70 110 L108 90 Q112 84 104 82 L78 92" stroke-width="7"/>
    <path class="icon-fill" d="M8 92 L20 88 L30 116 L18 120 Z"/>
  </g>

  <g class="stage-icon icon-maximise" transform="translate(1037 645)">
    <rect class="icon-tile" width="130" height="130"/>
    <rect class="icon-fill" x="18" y="98" width="16" height="22"/>
    <rect class="icon-fill" x="44" y="84" width="16" height="36"/>
    <rect class="icon-fill" x="70" y="66" width="16" height="54"/>
    <rect class="icon-fill" x="96" y="40" width="16" height="80"/>
    <path class="icon-line" d="M18 84 L98 18" stroke-width="6"/>
    <path class="icon-fill" d="M104 12 L84 14 L102 32 Z"/>
  </g>

  <g class="stage-icon icon-loyalty" transform="translate(538 829)">
    <rect class="icon-tile" width="130" height="130"/>
    <path class="icon-line" d="M34 80 A34 34 0 0 1 80 36" stroke-width="13" stroke-linecap="butt"/>
    <path class="icon-fill" d="M76 18 L100 38 L74 54 Z"/>
    <path class="icon-line" d="M96 50 A34 34 0 0 1 50 94" stroke-width="13" stroke-linecap="butt"/>
    <path class="icon-fill" d="M54 112 L30 92 L56 76 Z"/>
  </g>

  <g class="stage-icon icon-reactivation" transform="translate(637 321)">
    <rect class="icon-tile" width="130" height="130"/>
    <path class="icon-line" d="M42 36 A44 44 0 1 0 66 26" stroke-width="9"/>
    <path class="icon-fill" d="M32 20 L60 22 L42 48 Z"/>
  </g>
</svg>
</body>
</html>
```